OLUM Sign
OLUM leasing sign
#12 I'd like to go with this design with a few minor changes. Could you please change the font of Daniel Pruett to something that works better with the other font Office space? and can you remove the rectangles under the phone number? I promise i'll respond more quickly once i see the revisions.
additional comment on 23 -24. I think I like these for their clean simplicity (although they need the required information and the proper logo)
#23 ,#24 These looks different - good. Can you try a grey background, with correct logo (maybe in white). There is now an .eps file available. The sign must have phone number, "Office Space", and Realtor's name. use only the colors in logo, and black.
Dear PH, thanks for your valuable feedback.Will submit some more design options...regards,
will upload vector file. these designs are not what we are looking for. we want an eye catching creative design that doesn't look like a typical leasing sign.
Dear PH, Can you please upload the vector file (.ai or .eps) of the logo.Regards.

```html
<!DOCTYPE html>
<html lang="en">
<head>
<meta charset="utf-8">
<title>OLUM Leasing Sign</title>
<link rel="stylesheet" href="https://fonts.googleapis.com/css2?family=Open+Sans:wght@400;600&family=Russo+One&family=Archivo+Black&display=swap">
<style>
  :root {
    --red: #c8141c;
    --red-dark: #7a0a0e;
    --cream: #fffbe0;
    --cream-deep: #f6ecb4;
    --ink: #141414;
    --orange: #e2541a;
    --orange-dark: #9a2c08;
    --grey: #8a8a8a;
    --band-edge: #6e6e6e;
  }
  html, body {
    margin: 0;
    padding: 0;
    width: 1200px;
    height: 799px;
    overflow: hidden;
  }
  .sign {
    position: relative;
    width: 1200px;
    height: 799px;
    overflow: hidden;
    background: linear-gradient(180deg, var(--cream) 0%, var(--cream) 45%, var(--cream-deep) 100%);
    font-family: "Open Sans", sans-serif;
  }
  .sign__band {
    position: absolute;
    inset: 0;
    width: 1200px;
    height: 799px;
  }
  .sign__headline {
    position: absolute;
    top: 8px;
    left: 0;
    width: 1200px;
    text-align: center;
    color: #fff;
    font-family: "Open Sans", sans-serif;
    font-weight: 600;
    font-size: 104px;
    letter-spacing: 3px;
    line-height: 1.2;
  }
  .sign__offer {
    position: absolute;
    top: 240px;
    left: 0;
    width: 1200px;
    text-align: center;
    font-family: "Russo One", sans-serif;
    font-size: 104px;
    letter-spacing: 4px;
    color: var(--red);
    -webkit-text-stroke: 3px var(--red-dark);
    text-shadow: 3px 4px 0 rgba(0,0,0,0.25);
    line-height: 1.1;
  }
  .sign__phone {
    position: absolute;
    top: 385px;
    left: 118px;
    display: flex;
    align-items: center;
    gap: 40px;
  }
  .sign__phone-icon { width: 120px; height: 110px; }
  .sign__phone-number {
    font-family: "Archivo Black", sans-serif;
    font-size: 96px;
    color: var(--ink);
    letter-spacing: 2px;
    line-height: 1;
  }
  .sign__brand {
    position: absolute;
    left: 38px;
    top: 614px;
    width: 480px;
    height: 166px;
    border-radius: 22px;
    border: 3px solid #d8cfa0;
    background: linear-gradient(180deg, #fffdf0 0%, #f3e9b0 100%);
    display: flex;
    align-items: center;
    justify-content: center;
    gap: 22px;
  }
  .sign__brand-mark {
    width: 46px;
    height: 46px;
    background: var(--red);
  }
  .sign__brand-name {
    font-family: "Open Sans", sans-serif;
    font-weight: 600;
    font-size: 110px;
    color: var(--grey);
    letter-spacing: 4px;
    line-height: 1;
  }
  .sign__contact-label {
    position: absolute;
    top: 622px;
    right: 36px;
    font-family: "Open Sans", sans-serif;
    font-weight: 400;
    font-size: 54px;
    color: var(--ink);
    line-height: 1;
  }
  .sign__contact-rule {
    position: absolute;
    top: 698px;
    left: 540px;
    width: 648px;
    height: 4px;
    background: var(--orange);
  }
  .sign__contact-name {
    position: absolute;
    top: 712px;
    left: 540px;
    width: 648px;
    text-align: center;
    font-family: "Russo One", sans-serif;
    font-size: 60px;
    color: var(--orange);
    -webkit-text-stroke: 2px var(--orange-dark);
    letter-spacing: 3px;
    line-height: 1.1;
    white-space: nowrap;
  }
</style>
</head>
<body>
<div class="sign">
  <svg class="sign__band" viewBox="0 0 1200 799" aria-hidden="true">
    <defs>
      <linearGradient id="bandFill" x1="0" y1="0" x2="0" y2="1">
        <stop offset="0" stop-color="#e02a30"/>
        <stop offset="0.6" stop-color="#c8141c"/>
        <stop offset="1" stop-color="#8e0c12"/>
      </linearGradient>
      <radialGradient id="screw" cx="0.4" cy="0.4" r="0.6">
        <stop offset="0" stop-color="#ffffff"/>
        <stop offset="1" stop-color="#8a8a8a"/>
      </radialGradient>
    </defs>
    <path d="M0 0 H1200 V175 Q820 120 600 140 Q300 165 0 205 Z" fill="var(--band-edge)"/>
    <path d="M0 0 H1200 V162 Q820 108 600 128 Q300 152 0 192 Z" fill="url(#bandFill)"/>
    <circle cx="24" cy="24" r="8" fill="url(#screw)"/>
    <circle cx="1176" cy="24" r="8" fill="url(#screw)"/>
    <circle cx="24" cy="170" r="8" fill="url(#screw)"/>
    <circle cx="1176" cy="140" r="8" fill="url(#screw)"/>
  </svg>

  <div class="sign__headline">AVAILABLE</div>
  <div class="sign__offer">OFFICE SPACE</div>

  <div class="sign__phone">
    <svg class="sign__phone-icon" viewBox="0 0 120 110" aria-hidden="true">
      <path d="M8 34 Q10 10 60 10 Q110 10 112 34 L112 44 Q112 50 104 50 L86 50 Q80 50 80 42 L80 32 Q60 26 40 32 L40 42 Q40 50 34 50 L16 50 Q8 50 8 44 Z" fill="var(--red)"/>
      <path d="M30 48 L90 48 L106 100 Q106 106 100 106 L20 106 Q14 106 14 100 Z" fill="var(--red)"/>
      <circle cx="60" cy="78" r="20" fill="#f4d4d4"/>
      <circle cx="60" cy="78" r="7" fill="var(--red-dark)"/>
    </svg>
    <div class="sign__phone-number">215-555-0148</div>
  </div>

  <div class="sign__brand">
    <div class="sign__brand-mark"></div>
    <div class="sign__brand-name">OLUM</div>
  </div>

  <div class="sign__contact-label">Contact Person</div>
  <div class="sign__contact-rule"></div>
  <div class="sign__contact-name">DANIEL PRUETT</div>
</div>
</body>
</html>
```